Business Card Design

We need a business card design for a Non-Profit Christian Based Organization located in Milford, Pa.
Alder Ridge Helping Harbor
Is a Christ-centered organization dedicated to providing compassion and hope to homeless or near homeless, families and individuals, by meeting their basic and urgent need of food, clothing and shelter.
Updates
the logo is black and white
and must add the color green some where 00400
Industry/Entity Type
Clothing
Contact Information for Business Card
Alder Ridge Helping Harbor
P.O. Box 287
Hollis Glen, Pa 18452
Phone: (570) 413-CARE(2273)
Toll Free: (855) 413-CARE
email:Info@alderridgehh.org
email:Careline@alderridgehh.org
Our organization already has a logo.
Front of card:
Is a Christ-centered organization dedicated to providing compassion and hope to homeless or near homes, families and individual by meeting their basic and urgent need of food, clothing and shelter.(this is our Mission Statement)
On back of card:
'I was hungry and you gave me something to eat;
"I was thirsty and you gave me something to drink;
"I was a stranger and you invited me in."
Matthew 25:35
Color: Logo is black and white
Background color I would like a bright light green 00ff00(close to that)
I attached a sample of what I created on Quill Press but, I don't like the color green, nor the design (but I just wanted to give you and Idea of the Logo and Alder Ridge (one line) Helping Harbor (second line) in a different font thank you
Delia Rostova
Pr/Board of Directors

```html
<!DOCTYPE html>
<html lang="en">
<head>
<meta charset="utf-8">
<title>Alder Ridge Helping Harbor – Business Card</title>
<link rel="stylesheet" href="https://fonts.googleapis.com/css2?family=Open+Sans:wdth,wght@75..100,700&display=swap">
<style>
  :root {
    --backdrop: #6e5c4b;
    --card-green: #b5d334;
    --ink: #111111;
    --paper: #ffffff;
  }
  * { margin: 0; padding: 0; box-sizing: border-box; }
  html, body { width: 1200px; height: 1000px; overflow: hidden; }
  body {
    background: var(--backdrop);
    font-family: "Open Sans", Arial, sans-serif;
    font-weight: 700;
    font-stretch: 87.5%;
    color: var(--ink);
    position: relative;
  }
  .card {
    position: absolute;
    top: 50px;
    width: 513px;
    height: 898px;
    background: var(--card-green);
    overflow: hidden;
    box-shadow: 0 2px 6px rgba(0,0,0,0.35);
  }
  .card--quote { left: 60px; }
  .card--contact { left: 613px; }

  /* brand block */
  .brand { position: absolute; left: 0; width: 100%; text-align: center; }
  .brand__mark { display: block; margin: 0 auto; border-radius: 50%; background: var(--ink); }
  .brand__name { line-height: 1.15; color: var(--ink); }
  .card--quote .brand { top: 80px; }
  .card--quote .brand__mark { width: 320px; height: 320px; }
  .card--quote .brand__name { font-size: 38px; margin-top: 68px; }
  .card--contact .brand { top: 32px; }
  .card--contact .brand__mark { width: 220px; height: 220px; }
  .card--contact .brand__name { font-size: 30px; margin-top: 22px; }

  /* front: scripture */
  .scripture {
    position: absolute;
    top: 678px;
    left: 34px;
    right: 34px;
    text-align: center;
    font-size: 22px;
    line-height: 1.15;
  }
  .scripture__ref { color: var(--paper); display: block; }
  .card__footer-band {
    position: absolute; left: 0; bottom: 0; width: 100%; height: 76px;
    background: var(--paper);
  }

  /* back: mission + contact */
  .mission {
    position: absolute;
    top: 384px;
    left: 30px;
    right: 30px;
    text-align: center;
    font-size: 20px;
    line-height: 1.26;
  }
  .band { position: absolute; left: 0; width: 100%; display: flex; align-items: center; }
  .band--address { top: 537px; height: 108px; background: var(--ink); color: var(--paper); padding-left: 66px; font-size: 27px; line-height: 1.05; }
  .band--phone { top: 645px; height: 110px; background: var(--paper); padding-left: 32px; font-size: 24px; line-height: 1.15; }
  .band--email { top: 755px; height: 110px; background: var(--ink); color: var(--paper); padding-left: 38px; font-size: 24px; line-height: 1.15; }
  .band--trim { top: 878px; height: 17px; background: var(--card-green); }
  .band__icon { flex: none; margin-right: 16px; }
  .card--contact::after {
    content: ""; position: absolute; left: 0; top: 865px; width: 100%; height: 13px; background: var(--paper);
  }
</style>
</head>
<body>

<section class="card card--quote">
  <div class="brand">
    <span class="brand__mark"></span>
    <p class="brand__name">Alder Ridge<br>Helping Harbor</p>
  </div>
  <p class="scripture">
    "I was hungry and you gave me something to eat; “I was thirsty and you gave me something to drink; "I was a stranger and you invited me in."
    <span class="scripture__ref">Matthew 25:35</span>
  </p>
  <div class="card__footer-band"></div>
</section>

<section class="card card--contact">
  <div class="brand">
    <span class="brand__mark"></span>
    <p class="brand__name">Alder Ridge<br>Helping Harbor</p>
  </div>
  <p class="mission">Is a Christ-centered organization dedicated to providing compassion and hope to homeless or near homeless, families and individuals by meeting their basic and urgent need of food, clothing and shelter.</p>

  <div class="band band--address">
    <p>Alder Ridge Helping Harbor<br>P.O. Box 287 Hollis Glen, Pa 18452</p>
  </div>

  <div class="band band--phone">
    <svg class="band__icon" width="66" height="56" viewBox="0 0 66 56" aria-hidden="true">
      <path d="M4 14 C4 4 62 4 62 14 L62 20 L48 20 L48 13 L18 13 L18 20 L4 20 Z" fill="#111"/>
      <path d="M18 18 L48 18 L58 50 L8 50 Z" fill="#111"/>
      <g fill="#fff">
        <rect x="24" y="28" width="5" height="4"/><rect x="31" y="28" width="5" height="4"/><rect x="38" y="28" width="5" height="4"/>
        <rect x="23" y="35" width="5" height="4"/><rect x="31" y="35" width="5" height="4"/><rect x="39" y="35" width="5" height="4"/>
        <rect x="22" y="42" width="5" height="4"/><rect x="31" y="42" width="5" height="4"/><rect x="40" y="42" width="5" height="4"/>
      </g>
    </svg>
    <p>(570) 413-CARE(2273)<br>Toll Free: (855) 413-CARE</p>
  </div>

  <div class="band band--email">
    <svg class="band__icon" width="56" height="40" viewBox="0 0 56 40" aria-hidden="true">
      <rect x="1.5" y="1.5" width="53" height="37" fill="#fff" stroke="#fff" stroke-width="3"/>
      <path d="M3 4 L28 24 L53 4" fill="none" stroke="#111" stroke-width="3"/>
      <path d="M3 37 L21 19 M53 37 L35 19" fill="none" stroke="#111" stroke-width="3"/>
    </svg>
    <p>Info@alderridgehh.org<br>Careline@alderridgehh.org</p>
  </div>

  <div class="band band--trim"></div>
</section>

</body>
</html>
```